Letterhead and Business card for Construction company

We need a letterhead and business card with our new company logo. We are based in NY. We develop and build properties.

The design should incorporate some unique feature from the logo (shape, font...). it should look like an extension from it.

Design should be clean and elegant, professional, not too busy.

The letterhead should include:
Logo (attached)
Address
Phone
Email

Please find the attached logo images and AI file.

Target Market(s)

Construction industry professionals

Industry/Entity Type

Construction, Development

Font styles to use
Sans Serif

Colors

Designer to choose colors to be used in the design.

Requirements
Must have
• Design should incorporate logo elements, additional assets are welcome. I'd like to see some other shapes / images invorporated too.

```html
<!DOCTYPE html>
<html lang="en">
<head>
<meta charset="utf-8">
<title>Marlow Ridge Builders – Business Card</title>
<link rel="stylesheet" href="https://fonts.googleapis.com/css2?family=Montserrat:wght@400;500;700;800&display=swap">
<style>
  :root {
    --backdrop: #d4d4d4;
    --paper: #ffffff;
    --ink: #1d1b1c;
    --ink-soft: #3b3a3a;
    --accent: #f28a1e;
    --card-dark: #1e1c1d;
    --mark-dark: #5c5b5b;
    --rule: #6f6f6f;
  }
  * { box-sizing: border-box; margin: 0; padding: 0; }
  html, body { width: 1200px; height: 913px; overflow: hidden; }
  body {
    background: var(--backdrop);
    font-family: "Montserrat", sans-serif;
    color: var(--ink);
    display: flex;
    flex-direction: column;
    align-items: center;
    justify-content: center;
    gap: 40px;
  }
  .card {
    width: 640px;
    height: 366px;
    position: relative;
    box-shadow: 0 10px 24px rgba(0,0,0,0.22);
  }
  .card--front {
    background: var(--paper);
    display: flex;
    align-items: center;
  }
  .brand {
    width: 300px;
    padding-left: 54px;
    display: flex;
    align-items: center;
    gap: 12px;
  }
  .brand__square {
    width: 22px;
    height: 22px;
    background: var(--accent);
    flex: none;
  }
  .brand__name {
    font-weight: 800;
    font-size: 25px;
    line-height: 1.1;
    letter-spacing: 0.5px;
    text-transform: uppercase;
    color: var(--ink);
  }
  .divider {
    width: 1px;
    height: 210px;
    background: var(--rule);
    margin-top: 40px;
  }
  .details {
    padding-left: 38px;
    padding-bottom: 10px;
  }
  .details__name {
    font-weight: 800;
    font-size: 27px;
    letter-spacing: 0.3px;
    text-transform: uppercase;
    line-height: 1;
  }
  .details__role {
    font-size: 16px;
    color: var(--ink-soft);
    margin-top: 6px;
    margin-bottom: 18px;
  }
  .contact {
    list-style: none;
    font-size: 15px;
    line-height: 1;
  }
  .contact li {
    display: flex;
    align-items: center;
    gap: 12px;
    margin-bottom: 10px;
  }
  .contact svg { width: 16px; height: 16px; flex: none; }
  .address {
    font-style: normal;
    font-size: 16px;
    line-height: 1.35;
    margin-top: 14px;
  }
  .card--back {
    background: var(--card-dark);
    display: flex;
    align-items: center;
    justify-content: center;
    gap: 14px;
  }
  .card--back .brand__square { background: var(--mark-dark); width: 30px; height: 30px; }
  .card--back .brand__name {
    color: var(--mark-dark);
    font-size: 38px;
  }
</style>
</head>
<body>
  <section class="card card--front" aria-label="Business card front">
    <div class="brand">
      <span class="brand__square"></span>
      <span class="brand__name">Marlow Ridge<br>Builders</span>
    </div>
    <div class="divider"></div>
    <div class="details">
      <h1 class="details__name">Daniel Reyes</h1>
      <p class="details__role">Managing Director</p>
      <ul class="contact">
        <li>
          <svg viewBox="0 0 16 16" aria-hidden="true"><path d="M4 1.5l2.3 2.7-1.4 1.7c.8 1.9 2.3 3.4 4.2 4.2l1.7-1.4 2.7 2.3-1.6 2.2C6.5 13 3 9.5 1.8 3.1z" fill="var(--accent)"/></svg>
          044-987 654 321
        </li>
        <li>
          <svg viewBox="0 0 16 16" aria-hidden="true"><rect x="1" y="3" width="14" height="10" fill="var(--accent)"/><path d="M1 3l7 6 7-6" fill="none" stroke="#fff" stroke-width="1.2"/></svg>
          hello@marlowridge.com
        </li>
        <li>
          <svg viewBox="0 0 16 16" aria-hidden="true"><circle cx="8" cy="8" r="7" fill="var(--accent)"/><ellipse cx="8" cy="8" rx="3" ry="7" fill="none" stroke="#fff" stroke-width="1"/><path d="M1 8h14" stroke="#fff" stroke-width="1"/></svg>
          www.marlowridge.com
        </li>
      </ul>
      <address class="address">88, Harbor Street<br>New York, 10013</address>
    </div>
  </section>

  <section class="card card--back" aria-label="Business card back">
    <span class="brand__square"></span>
    <span class="brand__name">Marlow Ridge<br>Builders</span>
  </section>
</body>
</html>
```